Consumer Finance flyer

This flyer is being developed to help our outside sales people.

Please develop a master template flyer with key bullet points similar to uploaded file.

The main graphic will be replaced as we build out a flyer for each market segment. Example: Healthcare, Dental, Remodeling etc.
so we will keep the bullet point but replace the graphic for each custom vertical industry.

Need flyer to have an editable section at the bottom so the sales person can add their name and phone number and print the flyer.

please incorporate the FundLeafOne logo attached. So it will be branded fundleafone.

Industry/Entity Type

Dental

```html
<!DOCTYPE html>
<html lang="en">
<head>
<meta charset="utf-8">
<title>FundLeafOne – A New Financing Focus</title>
<link rel="stylesheet" href="https://fonts.googleapis.com/css2?family=Dosis:wght@500;600;700&family=Cormorant+Garamond:wght@500&family=Crimson+Text&display=swap">
<style>
  :root {
    --sky: #7fcbef;
    --orange: #f5a31d;
    --white: #ffffff;
    --ink: #111111;
    --photo-warm: #c9a98a;
    --photo-cool: #9aa7a3;
    --coin-bg: #f2ece2;
    --office-bg: #e6e8ea;
  }
  * { margin: 0; padding: 0; box-sizing: border-box; }
  html, body { width: 857px; height: 1200px; overflow: hidden; }
  body { background: var(--white); }
  .flyer {
    position: relative; width: 857px; height: 1200px;
    background: var(--sky); overflow: hidden;
    font-family: "Crimson Text", Georgia, serif; color: var(--ink);
  }
  .hero-photo {
    position: absolute; left: 0; top: 0; width: 857px; height: 352px;
    background: linear-gradient(135deg, #d88d78 0%, var(--photo-warm) 35%, var(--photo-cool) 70%, #c3b9a4 100%);
  }
  .hero-caption {
    position: absolute; right: 16px; top: 262px;
    text-align: right; color: var(--white); white-space: nowrap;
    font-family: "Dosis", Arial, sans-serif; font-weight: 600;
    font-size: 19px; line-height: 27.5px; letter-spacing: 1.4px;
  }
  .headline {
    font-family: "Dosis", Arial, sans-serif; font-weight: 700;
    position: absolute; line-height: 1; text-transform: uppercase;
  }
  .headline-new { left: 76px; top: 355px; font-size: 92px; color: var(--white); letter-spacing: 1px; }
  .headline-financing { left: 180px; top: 413px; font-size: 98px; color: var(--orange); letter-spacing: 0; }
  .headline-focus { left: 494px; top: 476px; font-size: 98px; color: var(--white); letter-spacing: 2px; }
  .tagline {
    position: absolute; left: 0; top: 562px; width: 857px; text-align: center;
    font-family: "Cormorant Garamond", Georgia, serif; font-weight: 500;
    font-size: 43px;
  }
  .intro {
    position: absolute; left: 48px; top: 633px; width: 218px;
    font-size: 15px; line-height: 16.6px; text-align: justify;
  }
  .coin-photo {
    position: absolute; left: 43px; top: 838px; width: 223px; height: 149px;
    background: radial-gradient(ellipse at 55% 55%, #d8b56a 0%, #e7d7b8 30%, var(--coin-bg) 60%);
  }
  .services {
    position: absolute; left: 48px; top: 995px; width: 230px;
    font-size: 15px; line-height: 16.8px; list-style: none;
  }
  .features {
    position: absolute; left: 320px; top: 631px; width: 255px; list-style: none;
    font-size: 13.6px; text-transform: uppercase; letter-spacing: 0.2px;
  }
  .features li { display: flex; align-items: center; height: 31.4px; white-space: nowrap; }
  .features li::before {
    content: ""; width: 10px; height: 10px; border-radius: 50%;
    background: var(--ink); margin-right: 7px; flex: none;
  }
  .office-photo {
    position: absolute; left: 583px; top: 638px; width: 245px; height: 457px;
    background: linear-gradient(160deg, #f4f4f4 0%, var(--office-bg) 45%, #8d949a 80%, #4a4f55 100%);
  }
  .contact {
    position: absolute; left: 44px; top: 1140px; white-space: nowrap;
    font-size: 24.5px;
  }
  .contact span + span { margin-left: 18px; }
  .brand {
    position: absolute; right: 30px; top: 1143px;
    display: flex; align-items: center; gap: 8px;
    font-family: "Crimson Text", Georgia, serif; font-size: 25px;
    letter-spacing: 2px; text-transform: uppercase; color: var(--ink);
  }
  .brand-dot { width: 14px; height: 14px; border-radius: 50%; background: var(--orange); }
</style>
</head>
<body>
<main class="flyer">
  <div class="hero-photo" role="img" aria-label="Close-up of hands counting dollar bills and coins"></div>
  <p class="hero-caption">You now have multiple financing and payment options to<br>help more clients today. You can now confidently tell the<br>world that you have fast and easy solutions for their needs</p>

  <h1>
    <span class="headline headline-new">A New</span>
    <span class="headline headline-financing">Financing</span>
    <span class="headline headline-focus">Focus</span>
  </h1>

  <h2 class="tagline">Helping you achieve customer satisfaction</h2>

  <p class="intro">Multiple lenders will process your clients with only ONE credit application. We will contact your clients for security and to help expedite the lending process for optimum performance and satisfaction.<br>Co-borrowers are welcome to help income profile of your clients. This can overcome reservations.</p>

  <div class="coin-photo" role="img" aria-label="Stack of gold coins on a light background"></div>

  <ul class="services">
    <li>We provide:</li>
    <li>Custom application website</li>
    <li>Online payment calculators.</li>
    <li>Back office status access.</li>
    <li>Live assistance.</li>
    <li>*multiple programs available*</li>
  </ul>

  <ul class="features">
    <li>Several interest free plans</li>
    <li>0% for 6 to 18 months</li>
    <li>Revolving lines of credit</li>
    <li>Term loans from 2 to 20yrs*</li>
    <li>National lenders compete</li>
    <li>Easy single page app</li>
    <li>Lenient requirements</li>
    <li>No default interest rates</li>
    <li>No prepayment penalties</li>
    <li>May request overnight</li>
    <li>Rates from 6.95%*</li>
    <li>Plus no credit app option</li>
    <li>Approvals in minutes</li>
    <li>May combine offers</li>
    <li>Credit approvals 24 to 48 hrs</li>
  </ul>

  <div class="office-photo" role="img" aria-label="Businessman on the phone working at a laptop"></div>

  <footer>
    <p class="contact"><span>800-555-0142</span><span>Dana Whitfield</span><span>dana@flo1.net</span></p>
    <div class="brand"><span>FundLeafOne</span><span class="brand-dot"></span></div>
  </footer>
</main>
</body>
</html>
```